New Business Card

Use website for color, logo and theme.

http://www.plumwickonline.com/

Back side of card should be programs listed on home page of website

1) Phone Number is (800) 555-0142 x23
2) Fax (240) 555-0187
3) Address is - 647 W Harlowe Street, Suite 312, Baltimore, MD 21201
4) NMLS #738516

```html
<!DOCTYPE html>
<html lang="en">
<head>
<meta charset="utf-8">
<title>Plumwick Financial Services – Business Card</title>
<link href="https://fonts.googleapis.com/css2?family=Source+Sans+3:wght@400;600&display=swap" rel="stylesheet">
<style>
  :root {
    --stage: #3a3a3a;
    --card-white: #f7f7f7;
    --brand-blue: #0b5599;
    --brand-gold: #a8913a;
    --ink: #3b3b3b;
    --photo-dark: #1f1f22;
    --photo-mid: #6b4a3a;
  }
  * { margin: 0; padding: 0; box-sizing: border-box; }
  html, body {
    width: 1200px; height: 750px; overflow: hidden;
    background: var(--stage);
    font-family: "Source Sans 3", sans-serif;
  }
  .card {
    position: absolute; top: 228px;
    width: 461px; height: 262px; overflow: hidden;
  }
  .card--front { left: 124px; background: var(--card-white); }
  .card--back { left: 618px; background: var(--brand-blue); }

  .front__blue-corner {
    position: absolute; right: 0; top: 0;
    width: 140px; height: 120px; background: var(--brand-blue);
  }
  .front__photo {
    position: absolute; right: 0; top: 0;
    width: 193px; height: 262px;
    background: linear-gradient(160deg, var(--photo-mid) 0%, var(--photo-mid) 40%, var(--photo-dark) 70%);
    clip-path: polygon(30% 0, 100% 0, 100% 100%, 0 100%, 12% 60%, 18% 30%);
  }
  .brand-name {
    position: absolute; left: 24px; top: 34px;
    display: flex; align-items: center; gap: 8px;
    font-weight: 600; font-size: 15px; color: var(--brand-blue);
    line-height: 1.15; width: 180px;
  }
  .brand-name__dot {
    flex: none; width: 14px; height: 14px; border-radius: 50%;
    background: var(--brand-gold);
  }
  .person { position: absolute; left: 25px; top: 122px; }
  .person__name { font-size: 17px; font-weight: 600; color: var(--brand-blue); line-height: 1.1; }
  .person__title { font-size: 12.5px; color: var(--brand-gold); line-height: 1.3; }
  .contact {
    position: absolute; left: 25px; top: 166px;
    font-size: 11px; color: var(--ink); line-height: 17.5px;
    list-style: none;
  }
  .contact__item { display: flex; align-items: center; gap: 5px; }
  .contact__icon { width: 13px; height: 12px; flex: none; }
  .contact__address { margin-top: 2px; line-height: 14px; }

  .back__brand {
    position: absolute; left: 0; right: 0; top: 92px;
    display: flex; justify-content: center; align-items: center; gap: 10px;
    font-size: 24px; font-weight: 600; color: #ffffff;
  }
  .back__brand .brand-name__dot { width: 20px; height: 20px; }
  .back__url {
    position: absolute; left: 0; right: 0; top: 214px;
    text-align: center; font-size: 11px; letter-spacing: 3.6px; color: #ffffff;
  }
</style>
</head>
<body>
  <section class="card card--front">
    <div class="front__blue-corner"></div>
    <div class="front__photo" role="img" aria-label="Portrait photo of the company founder in a dark suit and tie"></div>

    <div class="brand-name"><span class="brand-name__dot"></span><span>Plumwick Financial Services, Inc.</span></div>

    <div class="person">
      <p class="person__name">Marcus Hale</p>
      <p class="person__title">CEO/Founder</p>
    </div>

    <ul class="contact">
      <li>NMLS #738516</li>
      <li class="contact__item">
        <svg class="contact__icon" viewBox="0 0 24 24" aria-hidden="true"><path fill="#0b5599" d="M6.6 10.8a15.1 15.1 0 0 0 6.6 6.6l2.2-2.2c.3-.3.7-.4 1-.2 1.1.4 2.3.6 3.6.6.6 0 1 .4 1 1V20c0 .6-.4 1-1 1A17 17 0 0 1 3 4c0-.6.4-1 1-1h3.5c.6 0 1 .4 1 1 0 1.3.2 2.5.6 3.6.1.3 0 .7-.2 1z"/></svg>
        (800) 555-0142 x23
      </li>
      <li class="contact__item">
        <svg class="contact__icon" viewBox="0 0 24 22" aria-hidden="true"><rect x="6" y="1" width="12" height="7" fill="#0b5599"/><rect x="1" y="9" width="22" height="9" rx="2" fill="#0b5599"/><rect x="5" y="18" width="14" height="3" fill="#0b5599"/><rect x="6" y="12" width="12" height="2" fill="#ffffff"/></svg>
        (240) 555-0187
      </li>
      <li class="contact__address">647 W Harlowe Street<br>Suite 312, Baltimore, MD 21201</li>
    </ul>
  </section>

  <section class="card card--back">
    <div class="back__brand"><span class="brand-name__dot"></span><span>Plumwick Financial Services</span></div>
    <p class="back__url">www.plumwickonline.com</p>
  </section>
</body>
</html>
```